Wine label for South African wine

modern, creative wine label name: Dravenholt The Varnex-Bund GmbH - International Wines one of the leading independent providers of inexpensive wines from around the world. The company focuses entirely on this dynamic, constantly evolving wine market, and our customers can therefore take full advantage of a complete supply chain management for themselves, including: * http://www.varnexbund.example/img/rebe.jpg procuring wines from the major producing regions around the globe * logistics and processing * wage filling and packaging * dealcoholization of wines for gastronomic purposes * design of exclusive client and proprietary brands, the target market / target group: the International market design Features; Modern, simple, meaningful, unique; Colors: gold, black, red;

Target Market(s)

Off Trade

Industry/Entity Type

Union

Font styles to use
Serif
Script

Requirements
Must have
• Modern, simple, meaningful, unique colors: gold, black, red varieties: Cab Sauv, Chard, Chenin, Merlot, Merlot Rose, Pinotage, Pinotage Rose, Shiraz, Red, Rose, White Non transparent max. Size: 12 x 9 cm data on VE: name brand, variety, country; WITHOUT Year

```html
<!DOCTYPE html>
<html lang="en">
<head>
<meta charset="utf-8">
<title>Dravenholt – Wine Labels</title>
<link rel="stylesheet" href="https://fonts.googleapis.com/css2?family=EB+Garamond:wght@400;500&display=swap">
<style>
  :root {
    --backdrop: #d9d9d9;
    --paper: #fbf8ee;
    --ink: #1d1a17;
    --wine-red: #c0142c;
    --gold: #c9a33a;
    --gold-deep: #8a6a1c;
    --rule: #6f6a62;
  }
  * { box-sizing: border-box; margin: 0; padding: 0; }
  html, body { width: 1200px; height: 1000px; overflow: hidden; }
  body {
    background: radial-gradient(ellipse at center, #f4f4f4 0%, var(--backdrop) 70%, #b9b9b9 100%);
    font-family: "EB Garamond", "Times New Roman", serif;
    color: var(--ink);
    position: relative;
  }
  .label {
    position: absolute;
    top: 258px;
    height: 562px;
    background: var(--paper);
    box-shadow: 0 1px 4px rgba(0,0,0,.18);
  }
  .label--chardonnay { left: 155px; width: 400px; }
  .label--cabernet { left: 652px; width: 406px; }

  .emblem {
    position: absolute;
    top: 90px;
    width: 156px; height: 156px;
    border-radius: 50%;
    background: radial-gradient(circle at 45% 40%, #f0d27a 0%, var(--gold) 55%, var(--gold-deep) 100%);
  }
  .label--chardonnay .emblem { left: 125px; }
  .label--cabernet .emblem { left: 128px; }

  .brand-name,
  .variety,
  .producer,
  .origin {
    position: absolute;
    left: 0;
    width: 100%;
    text-align: center;
    line-height: 1;
    white-space: nowrap;
  }
  .label--chardonnay .brand-name,
  .label--chardonnay .variety,
  .label--chardonnay .producer,
  .label--chardonnay .origin { left: 22px; width: 358px; }

  .brand-name {
    top: 280px;
    font-size: 44px;
    font-weight: 400;
    letter-spacing: 0;
  }
  .variety {
    top: 332px;
    color: var(--wine-red);
    font-size: 23px;
    letter-spacing: .3px;
  }
  .producer { font-size: 19px; }
  .producer span {
    border-bottom: 1.5px solid var(--ink);
    padding-bottom: 3px;
  }
  .origin { font-size: 15px; }
  .label--chardonnay .producer { top: 474px; }
  .label--chardonnay .origin { top: 502px; }
  .label--cabernet .producer { top: 442px; }
  .label--cabernet .origin { top: 468px; }

  /* Chardonnay frame and side strip */
  .frame-left {
    position: absolute; left: 22px; top: 0; bottom: 0;
    border-left: 1px solid var(--rule);
  }
  .side-strip {
    position: absolute; left: 380px; top: 0; bottom: 0; width: 20px;
    border-left: 1px solid var(--rule);
  }
  .side-cell {
    position: absolute; left: 0; width: 20px;
    display: flex; align-items: center; justify-content: center;
    overflow: hidden;
  }
  .side-cell + .side-cell { border-top: 1px solid var(--rule); }
  .side-cell span {
    transform: rotate(-90deg);
    white-space: nowrap;
    font-size: 13px;
  }
  .side-cell--bottler { top: 0; height: 318px; }
  .side-cell--bottler span { font-size: 8.5px; letter-spacing: 0; }
  .side-cell--abv { top: 318px; height: 142px; }
  .side-cell--volume { top: 460px; height: 102px; }

  /* Cabernet bottom band */
  .info-band {
    position: absolute;
    left: 8px; right: 8px; top: 487px; height: 66px;
    border-top: 1.5px dotted var(--rule);
    border-bottom: 1.5px dotted var(--rule);
    display: grid;
    grid-template-columns: 95px 215px 1fr;
    font-size: 15px;
  }
  .info-band .cell {
    display: flex; align-items: center; justify-content: center;
    border-left: 1px solid var(--rule);
  }
  .info-band .cell:first-child { border-left: none; }
</style>
</head>
<body>
  <section class="label label--chardonnay">
    <div class="frame-left"></div>
    <div class="emblem" role="img" aria-label="Dravenholt gold emblem"></div>
    <h1 class="brand-name">DRAVENHOLT</h1>
    <p class="variety">CHARDONNAY</p>
    <p class="producer"><span>THE VARNEX-BUND GMBH</span></p>
    <p class="origin">PRODUCT OF GERMANY</p>
    <div class="side-strip">
      <div class="side-cell side-cell--bottler"><span>VINTED AND BOTTLED BY DRAVENHOLT THE VARNEX-BUND GMBH</span></div>
      <div class="side-cell side-cell--abv"><span>% ALC BY VOL</span></div>
      <div class="side-cell side-cell--volume"><span>750ML</span></div>
    </div>
  </section>

  <section class="label label--cabernet">
    <div class="emblem" role="img" aria-label="Dravenholt gold emblem"></div>
    <h1 class="brand-name">DRAVENHOLT</h1>
    <p class="variety">CABERNET SAUVIGNON</p>
    <p class="producer"><span>THE VARNEX-BUND GMBH</span></p>
    <p class="origin">PRODUCT OF GERMANY</p>
    <div class="info-band">
      <div class="cell"></div>
      <div class="cell">% ALC BY VOL</div>
      <div class="cell">750ML</div>
    </div>
  </section>
</body>
</html>
```